High end business card design for custom homebuilding company

Looking for a high end business card design that is unique and elegant. Can use embossing, foil printing, laser die cutting, or any high end printing technique or high end paper. Will upload current design so you can see the logo and what we are using currently, but we want something more unique and elegant. I included our logo to help with design.

Target Market(s)

High end custom home buyers of $1.5 million plus homes. Also real estate developers of high end communities.

Industry/Entity Type

Business

Contact Information for Business Card

Double sided. We want something very elegant and expensive looking. We are looking to incorporate a combination of perhaps linen paper or a high end paper, with foil stamping or embossing/debossing to make the card look unique, but still elegant. We tend to use blacks and golds, but are open to any ideas. Looking for creative and unique design.

Colors

Designer to choose colors to be used in the design.

Requirements
Must have
• High end, elegant look. Can use foil, embossing, or high end papers like linen. We want to make the card unique and interesting, but elegant and expensive looking.
Nice to have
• I am including just some cards I saw that looked interesting for one reason or another. I like a clean elegant design and like both the clean white style, and the blacks. So not sure if we want a black design or white. Would like to see both.

```html
<!DOCTYPE html>
<html lang="en">
<head>
<meta charset="utf-8">
<title>Meridian Ridge Homes – Business Card</title>
<link rel="stylesheet" href="https://fonts.googleapis.com/css2?family=Courgette&family=Kaushan+Script&display=swap">
<style>
  :root {
    --gold-deep: #a8925a;
    --gold-mid: #c2ad6d;
    --gold-light: #e6de95;
    --gold-icon: #b8a155;
    --ink: #141210;
    --brand-ink: #3a3426;
    --paper: #ffffff;
  }
  html, body {
    margin: 0;
    padding: 0;
    width: 1200px;
    height: 686px;
    overflow: hidden;
    background: var(--paper);
  }
  .card {
    position: relative;
    width: 1200px;
    height: 686px;
    background: var(--paper);
    overflow: hidden;
    font-family: "Courgette", cursive;
    color: var(--ink);
  }
  .gold-panel {
    position: absolute;
    left: 0;
    top: 0;
    width: 340px;
    height: 686px;
  }
  .brand {
    position: absolute;
    left: 250px;
    top: 56px;
    display: flex;
    align-items: center;
    gap: 18px;
  }
  .brand-dot {
    width: 58px;
    height: 58px;
    border-radius: 50%;
    background: var(--gold-mid);
  }
  .brand-name {
    font-family: "Courgette", cursive;
    font-size: 62px;
    line-height: 1;
    color: var(--brand-ink);
    letter-spacing: 1px;
  }
  .contact-item {
    position: absolute;
    display: flex;
    align-items: center;
    font-size: 38px;
    line-height: 1.05;
    letter-spacing: 1px;
    white-space: nowrap;
  }
  .contact-icon {
    flex: none;
  }
  .contact-item.mobile { left: 152px; top: 226px; gap: 20px; }
  .contact-item.desk   { left: 200px; top: 316px; gap: 24px; }
  .contact-item.email  { left: 240px; top: 414px; gap: 4px; font-size: 35px; }
  .contact-item.office { left: 276px; top: 508px; gap: 14px; font-size: 35px; white-space: normal; align-items: flex-start; }
  .contact-item.web    { left: 330px; top: 612px; gap: 12px; }
  .office-text { width: 300px; line-height: 0.98; }
  .holder {
    position: absolute;
    right: 12px;
    top: 236px;
    text-align: right;
    font-family: "Kaushan Script", cursive;
  }
  .holder-name {
    font-size: 48px;
    line-height: 1;
    letter-spacing: 2px;
  }
  .holder-position {
    font-size: 36px;
    line-height: 1;
    letter-spacing: 2px;
    margin-top: 2px;
  }
</style>
</head>
<body>
<div class="card">
  <svg class="gold-panel" viewBox="0 0 340 686" aria-hidden="true">
    <defs>
      <linearGradient id="panelGold" x1="0" y1="0" x2="1" y2="0">
        <stop offset="0" stop-color="#a58f57"/>
        <stop offset="0.28" stop-color="#b9a366"/>
        <stop offset="0.38" stop-color="#e3dc92"/>
        <stop offset="0.46" stop-color="#e9e39c"/>
        <stop offset="0.56" stop-color="#bfa96a"/>
        <stop offset="1" stop-color="#a8925a"/>
      </linearGradient>
    </defs>
    <polygon points="0,0 312,0 101,207 333,686 0,686" fill="url(#panelGold)"/>
    <polyline points="312,0 101,207 333,686" fill="none" stroke="#efe9b8" stroke-width="3"/>
  </svg>

  <div class="brand">
    <span class="brand-dot"></span>
    <span class="brand-name">Meridian Ridge Homes</span>
  </div>

  <div class="contact-item mobile">
    <svg class="contact-icon" width="34" height="68" viewBox="0 0 34 68" aria-hidden="true">
      <rect x="4" y="0" width="4" height="14" fill="var(--gold-icon)"/>
      <rect x="2" y="12" width="30" height="54" rx="3" fill="var(--gold-icon)"/>
      <rect x="7" y="18" width="20" height="14" fill="#efe7b0"/>
      <g fill="#efe7b0">
        <rect x="7" y="37" width="5" height="4"/><rect x="14.5" y="37" width="5" height="4"/><rect x="22" y="37" width="5" height="4"/>
        <rect x="7" y="45" width="5" height="4"/><rect x="14.5" y="45" width="5" height="4"/><rect x="22" y="45" width="5" height="4"/>
        <rect x="7" y="53" width="5" height="4"/><rect x="14.5" y="53" width="5" height="4"/><rect x="22" y="53" width="5" height="4"/>
      </g>
    </svg>
    <span>+123-456-7890</span>
  </div>

  <div class="contact-item desk">
    <svg class="contact-icon" width="34" height="58" viewBox="0 0 34 58" aria-hidden="true">
      <path d="M4 14 Q17 -2 30 14 L26 18 Q17 10 8 18 Z" fill="var(--gold-icon)"/>
      <path d="M10 18 L24 18 L28 56 L6 56 Z" fill="var(--gold-icon)"/>
      <circle cx="17" cy="32" r="4" fill="#efe7b0"/>
    </svg>
    <span>1234567</span>
  </div>

  <div class="contact-item email">
    <svg class="contact-icon" width="50" height="40" viewBox="0 0 50 40" aria-hidden="true">
      <rect x="2" y="2" width="46" height="36" fill="#f4efcf" stroke="var(--gold-icon)" stroke-width="3"/>
      <polyline points="2,2 25,24 48,2" fill="none" stroke="var(--gold-icon)" stroke-width="3"/>
      <polyline points="2,38 19,19 M48,38 31,19" fill="none" stroke="var(--gold-icon)" stroke-width="2"/>
    </svg>
    <span>name@email.com</span>
  </div>

  <div class="contact-item office">
    <svg class="contact-icon" width="32" height="68" viewBox="0 0 32 68" aria-hidden="true">
      <path d="M16 66 L3 22 A14 14 0 1 1 29 22 Z" fill="var(--gold-icon)"/>
      <ellipse cx="16" cy="13" rx="4" ry="7" fill="#f1eab8"/>
    </svg>
    <span class="office-text">office address of holder</span>
  </div>

  <div class="contact-item web">
    <svg class="contact-icon" width="50" height="50" viewBox="0 0 50 50" aria-hidden="true">
      <g fill="none" stroke="var(--gold-icon)" stroke-width="3">
        <circle cx="25" cy="25" r="22"/>
        <ellipse cx="25" cy="25" rx="10" ry="22"/>
        <line x1="25" y1="3" x2="25" y2="47"/>
        <line x1="3" y1="25" x2="47" y2="25"/>
        <path d="M7 13 H43 M7 37 H43"/>
      </g>
    </svg>
    <span>companywebsite.com</span>
  </div>

  <div class="holder">
    <div class="holder-name">Holder Name</div>
    <div class="holder-position">Position</div>
  </div>
</div>
</body>
</html>
```